Lantern's Pick CBD Packaging and Branding

We are looking for packaging designs for a new doctor focused CBD brand that is disease specific formulations (i.e. Bone and Joint Formula, Pelvic Formula, Pain Formula, Inflammation Formula, ect.) We would like the first packaging prototype to be our Pain Formulation. Our tagline is, "The Lantern's Pick" & we would also like the phrase, "Life. Balanced." - We are looking for our Logo to be on the box as well. We currently need a logo as well. We would like the letters "QX" to be more prominent than "vita" Our first product will be SoftGels and the active ingredient list can be made up at the moment. Our brand and packaging needs to convey authority, trust and scientific knowledge (since all of our formulations are created by researched and renowned doctors and scientists), but we also don't want to be too clinical feeling, so adding a modern touch. Attached are some sample designs for reference (none are the final iteration) as well as some vectorized art.

Target Market(s)

40-60 year old patients

Industry/Entity Type

Medical And Science

Logo Text

QX Vita

Requirements
Must have
• Clean, professional and trusting medical designs with a modern touch. New logo incorporated into the design.
Should not have
• Not too clinical feeling - Not pharmaceutical

```html
<!DOCTYPE html>
<html lang="en">
<head>
<meta charset="utf-8">
<title>QX Vita — Comfort Soft Gels Carton</title>
<link rel="stylesheet" href="https://fonts.googleapis.com/css2?family=Quicksand:wght@400;500;600&display=swap">
<style>
  :root {
    --backdrop: #b3bcc1;
    --panel: #eef0f1;
    --teal: #2f8c88;
    --teal-deep: #247a76;
    --grey-text: #8e9497;
    --white: #ffffff;
    --figure-orange: #e2925f;
    --figure-teal: #4fa5a3;
    --figure-violet: #7c5aa8;
    --figure-pink: #c25a94;
  }
  * { box-sizing: border-box; margin: 0; padding: 0; }
  html, body { width: 1200px; height: 900px; overflow: hidden; }
  body {
    background: var(--backdrop);
    font-family: "Quicksand", sans-serif;
    position: relative;
  }
  .panel {
    position: absolute;
    background: var(--panel);
    overflow: hidden;
  }
  .panel--top { left: 350px; top: 80px; width: 260px; height: 170px; }
  .panel--tagline { left: 160px; top: 270px; width: 170px; height: 560px; }
  .panel--front { left: 350px; top: 270px; width: 260px; height: 560px; }
  .panel--info { left: 630px; top: 270px; width: 170px; height: 560px; }
  .panel--back { left: 820px; top: 270px; width: 260px; height: 560px; }

  .formula-band {
    position: absolute; left: 0; right: 0; bottom: 0; height: 62px;
    background: var(--teal);
    color: var(--white);
    font-size: 14px; font-weight: 500; letter-spacing: 0.5px;
    display: flex; align-items: center; justify-content: center;
    text-transform: uppercase;
  }

  .brand { position: absolute; text-align: left; white-space: nowrap; }
  .brand__name {
    color: var(--teal);
    font-weight: 500;
    font-size: 38px;
    line-height: 1;
    letter-spacing: 1px;
  }
  .brand__line {
    color: var(--grey-text);
    font-size: 9px;
    letter-spacing: 2.4px;
    text-transform: uppercase;
    margin-top: 4px;
  }
  .panel--front .brand { right: 20px; top: 86px; }
  .panel--back .brand { right: 16px; top: 70px; }
  .panel--back .brand__name { font-size: 28px; }
  .panel--back .brand__line { font-size: 7px; letter-spacing: 1.6px; }
  .panel--top .brand { left: 50%; top: 34px; transform: translateX(-50%); text-align: center; }
  .panel--top .brand__name { font-size: 30px; }
  .top-tagline {
    position: absolute; left: 0; right: 0; top: 112px;
    text-align: center; color: var(--grey-text);
    font-size: 15px; font-weight: 600; letter-spacing: 2px;
  }

  .product {
    position: absolute;
    color: var(--teal);
    white-space: nowrap;
  }
  .product__name { font-size: 28px; font-weight: 600; letter-spacing: 0.5px; line-height: 1; }
  .product__use { font-size: 12px; color: var(--grey-text); text-transform: uppercase; margin-top: 1px; }
  .product__specs { list-style: none; font-size: 14px; font-weight: 600; line-height: 1.3; margin-top: 14px; }
  .panel--front .product { left: 96px; top: 330px; }
  .panel--back .product { left: 112px; top: 300px; }
  .panel--back .product__name { font-size: 24px; }
  .panel--back .product__use { font-size: 11px; }
  .panel--back .product__specs { font-size: 13px; }

  .figure {
    position: absolute;
    border-radius: 40px 40px 14px 14px;
    background: linear-gradient(to bottom,
      var(--figure-orange) 0%, var(--figure-orange) 14%,
      var(--figure-teal) 32%, var(--figure-violet) 62%, var(--figure-pink) 100%);
    opacity: 0.9;
  }
  .panel--front .figure { left: -10px; top: 70px; width: 80px; height: 430px; }
  .panel--back .figure { left: 22px; top: 40px; width: 72px; height: 460px; }
  .panel--info .figure { right: -28px; top: 90px; width: 46px; height: 400px; }

  .tagline {
    position: absolute; left: 20px; top: 36px;
    color: var(--teal); font-size: 19px; font-weight: 600; line-height: 1.5;
  }
  .stacked-line {
    position: absolute; left: 20px; top: 330px;
    list-style: none;
    color: var(--grey-text); font-size: 15px; letter-spacing: 4px; line-height: 1.6;
    text-transform: uppercase;
  }

  .info-copy {
    position: absolute; left: 18px; top: 50px; width: 110px;
    font-size: 10px; line-height: 1.45; color: #3e4447;
  }
  .panel--info .brand { left: 18px; top: 410px; }
  .panel--info .brand__name { font-size: 18px; }
  .panel--info .brand__line { font-size: 5px; letter-spacing: 1px; }
</style>
</head>
<body>
  <section class="panel panel--top" aria-label="Carton top flap">
    <div class="brand">
      <div class="brand__name">QX Vita</div>
      <div class="brand__line">The Lantern's Pick</div>
    </div>
    <p class="top-tagline">Life. Balanced.</p>
  </section>

  <section class="panel panel--tagline" aria-label="Carton left side">
    <p class="tagline">Life.<br>Balanced.</p>
    <ul class="stacked-line">
      <li>The</li>
      <li>Lantern's</li>
      <li>Pick</li>
    </ul>
    <div class="formula-band">Immune Formula</div>
  </section>

  <section class="panel panel--front" aria-label="Carton front">
    <div class="figure" role="img" aria-label="Colourful anatomical illustration of a standing human figure showing muscle groups"></div>
    <div class="brand">
      <div class="brand__name">QX Vita</div>
      <div class="brand__line">The Lantern's Pick</div>
    </div>
    <div class="product">
      <h1 class="product__name">COMFORT</h1>
      <p class="product__use">Paint Relief</p>
      <ul class="product__specs">
        <li>Soft Gels</li>
        <li>60mg CBD</li>
        <li>30CT</li>
      </ul>
    </div>
    <div class="formula-band">Immune Formula</div>
  </section>

  <section class="panel panel--info" aria-label="Carton right side">
    <p class="info-copy">Each soft gel delivers a measured dose of broad spectrum hemp extract, blended by physicians to ease everyday aches. Take one gel daily with food, or as your doctor directs. Store cool and dry, away from light.</p>
    <div class="figure" role="img" aria-label="Edge of the colourful anatomical human figure illustration wrapping from the front"></div>
    <div class="brand">
      <div class="brand__name">QX Vita</div>
      <div class="brand__line">The Lantern's Pick</div>
    </div>
    <div class="formula-band">Immune Formula</div>
  </section>

  <section class="panel panel--back" aria-label="Carton back">
    <div class="figure" role="img" aria-label="Colourful anatomical illustration of a standing human figure with arms slightly open"></div>
    <div class="brand">
      <div class="brand__name">QX Vita</div>
      <div class="brand__line">The Lantern's Pick</div>
    </div>
    <div class="product">
      <h2 class="product__name">COMFORT</h2>
      <p class="product__use">Paint Relief</p>
      <ul class="product__specs">
        <li>Soft Gels</li>
        <li>60mg CBD</li>
        <li>30CT</li>
      </ul>
    </div>
    <div class="formula-band">Immune Formula</div>
  </section>
</body>
</html>
```